Stroomwacht Powerpoint - presentation slides for energy management tool

We need a Powerpoint presentation lay-out which matches our logo from Stroomwacht.nl. 10 slides variations minimum, enough for a full professional presentation to potential clients.
Stroomwacht is a Dutch energymanagement tool for corporate real estate and housing agency. Our clients are Social houseing organisation, real estate owers, property managers and property developers.
Target Market(s)
real estate owners
Property manage
Font styles to use
Sans Serif
Colors
f78f20
0255a3
Requirements
Must have
- Stroomwacht logo colors and style
#F37122 orange
#00345D darkblue
Nice to have
- Professional look, background not white in every slide
Should not have
- wrong color orange and blue.

```html
<!DOCTYPE html>
<html lang="nl">
<head>
<meta charset="utf-8">
<title>Stroomwacht – presentatie lay-out</title>
<link rel="stylesheet" href="https://fonts.googleapis.com/css2?family=Montserrat:wght@400;500;600;700;800&display=swap">
<style>
:root{
  --orange:#F37122;
  --orange-light:#f78f20;
  --navy:#00345D;
  --blue:#0255a3;
  --ink:#1c2b3a;
  --muted:#4f5b68;
  --stage:#f1f2f4;
  --board:#dedede;
  --line:#c9ced4;
  --panel:#2a3a4f;
  --soft:#e3e8ee;
}
html,body{margin:0;width:1200px;height:2400px;overflow:hidden}
body{position:relative;background:var(--board);font-family:'Montserrat',sans-serif;color:var(--ink)}
.defs{position:absolute;width:0;height:0}
.stage{position:absolute;left:0;top:0;width:1200px;height:635px;background:var(--stage)}

.slide{position:absolute;width:347px;height:195px;overflow:hidden;background:#fff;box-shadow:0 1px 3px rgba(0,0,0,.08)}
.c1{left:37px}.c2{left:426px}.c3{left:815px}
.r1{top:727px}.r2{top:995px}.r3{top:1264px}.r4{top:1532px}.r5{top:1823px}.r6{top:2097px}
.hero{left:310px;top:100px;transform:scale(1.671);transform-origin:0 0;box-shadow:0 6px 24px rgba(0,0,0,.15)}

.fill{position:absolute;left:0;top:0;width:100%;height:100%}
.abs{position:absolute}

/* brand */
.logo{position:absolute;display:flex;align-items:center;gap:4px;font-weight:600;color:var(--orange);font-size:13px;letter-spacing:-.2px;white-space:nowrap}
.logo-dot{width:15px;height:15px;border-radius:50%;background:var(--navy);flex:none}
.logo.small{font-size:7px;gap:2px}
.logo.small .logo-dot{width:8px;height:8px}
.logo.corner{right:12px;top:10px}
.partner{position:absolute;display:flex;flex-direction:column;align-items:center;gap:1px;font-size:4.5px;font-weight:700;color:var(--blue);letter-spacing:.2px}
.partner-dot{width:11px;height:11px;border-radius:50%;background:var(--blue)}

/* cover */
.cover-title{position:absolute;left:0;top:38px;width:100%;margin:0;text-align:center;font-size:17px;font-weight:800;color:#fff;letter-spacing:.1px}
.accent{color:var(--orange)}
.cover-sub{position:absolute;left:0;top:66px;width:100%;margin:0;text-align:center;font-size:6px;line-height:1.45;font-weight:500;color:#fff}
.wave-orange{fill:none;stroke:var(--orange);stroke-width:4}
.wave-grey{fill:none;stroke:#b9bec5;stroke-width:1.5}

/* content slides */
.slide-heading{position:absolute;left:38px;top:26px;margin:0;font-size:11.5px;font-weight:800;line-height:1.08;color:var(--navy)}
.slide-heading.rule::after{content:"";display:block;width:26px;height:2px;background:var(--orange);margin-top:4px}
.sub-heading{margin:0 0 4px;font-size:8px;font-weight:700;color:var(--navy);line-height:1.1}
.body-text{margin:0 0 3px;font-size:5px;line-height:1.5;color:var(--muted)}

/* interface mock-ups */
.ui{position:absolute;display:flex;background:#fff;border:1px solid #d5dbe2;border-radius:2px;overflow:hidden;box-sizing:border-box}
.ui-side{width:18%;background:var(--panel);padding:5px 3px;display:flex;flex-direction:column;gap:4px;box-sizing:border-box}
.ui-side i{display:block;height:2px;background:rgba(255,255,255,.35)}
.ui-side i.on{background:var(--orange)}
.ui-main{flex:1;padding:4px;display:flex;flex-direction:column;gap:3px;box-sizing:border-box}
.ui-top{height:5px;background:var(--blue);border-radius:1px}
.ui-row{display:block;height:2px;background:var(--soft)}
.ui-row.short{width:55%}
.ui-cards{display:flex;gap:3px}
.ui-cards i{flex:1;height:9px;background:#eef2f6;border-top:1.5px solid var(--blue)}
.ui-cards i:nth-child(2){border-top-color:var(--orange)}
.ui-chart{flex:1;display:flex;align-items:flex-end;gap:1.5px;min-height:10px}
.ui-chart i{flex:1;background:var(--blue);opacity:.85}
.ui-chart i:nth-child(3n){background:var(--orange)}
.ui-photo{height:16px;width:40%;background:linear-gradient(135deg,#9aa3ae,#6c7785)}
.laptop{position:absolute}
.laptop .lid{position:absolute;left:8px;right:8px;top:0;bottom:6px;background:#1d1f22;border-radius:3px 3px 0 0;padding:4px;box-sizing:border-box}
.laptop .lid .ui{position:static;width:100%;height:100%;border:none}
.laptop .base{position:absolute;left:0;right:0;bottom:0;height:6px;background:linear-gradient(180deg,#c8ccd1,#9ea4ab);border-radius:0 0 4px 4px}

.slide-footer{position:absolute;left:0;right:0;bottom:0;height:8px;display:flex;align-items:center;font-size:4.2px;color:#fff}
.footer-site{height:100%;width:94px;background:var(--orange);clip-path:polygon(0 0,100% 0,94% 100%,0 100%);display:flex;align-items:center;padding-left:14px;box-sizing:border-box;font-weight:700;letter-spacing:.2px}
.footer-bar{flex:1;height:100%;margin-left:4px;background:var(--navy);clip-path:polygon(6px 0,100% 0,100% 100%,0 100%);display:flex;align-items:center;justify-content:flex-end;padding-right:8px;box-sizing:border-box}
.footer-page{width:14px;height:100%;background:var(--orange);margin-left:2px;display:flex;align-items:center;justify-content:center;font-weight:700}

/* flow */
.flow{position:absolute;left:40px;top:76px;display:flex;align-items:center;gap:5px}
.flow-meter{width:34px;height:34px;border-radius:50%;border:2px solid var(--navy);box-sizing:border-box;background:#fff;display:flex;flex-direction:column;align-items:center;justify-content:center;gap:2px}
.flow-meter i{display:block;width:16px;height:4px;background:var(--orange)}
.flow-meter b{display:block;width:8px;height:8px;border-radius:50%;border:1.5px solid var(--navy)}
.flow-step{width:26px;height:16px;background:var(--orange);color:#fff;font-size:7px;font-weight:800;display:flex;align-items:center;padding-left:4px;box-sizing:border-box;clip-path:polygon(0 0,72% 0,100% 50%,72% 100%,0 100%)}
.flow-phone{width:20px;height:36px;border:2px solid var(--navy);border-radius:4px;box-sizing:border-box;background:#fff;display:flex;align-items:center;justify-content:center}
.flow-phone i{display:block;width:10px;height:10px;border:1.5px solid var(--navy);box-sizing:border-box}
.flow-phone i.dial{border-radius:50%}
.flow-screen{width:40px;height:28px;border:2px solid var(--navy);border-radius:2px;box-sizing:border-box;background:#fff;padding:3px;display:flex;flex-direction:column;gap:2px}
.flow-screen i{display:block;height:2px;background:var(--soft)}
.flow-screen i:first-child{background:var(--orange);width:60%}

/* benefits */
.benefits{position:absolute;left:28px;right:18px;top:58px;display:flex;gap:12px}
.benefit{flex:1;text-align:center}
.benefit-icon{height:30px;display:flex;align-items:flex-end;justify-content:center;gap:2px;margin-bottom:6px}
.benefit h3{margin:0;font-size:6.2px;font-weight:700;color:var(--navy)}
.benefit .tag{margin:1px 0 3px;font-size:4.6px;font-weight:600;color:var(--orange);line-height:1.3}
.benefit .body-text{font-size:4.5px}
.bar{width:3px;background:var(--navy)}

/* partners */
.badges{position:absolute;left:38px;right:28px;bottom:20px;display:flex;align-items:center;gap:10px}
.badge{height:14px;flex:1;border-radius:7px;background:#fff;border:1.5px solid var(--blue);box-sizing:border-box;position:relative}
.badge::before{content:"";position:absolute;left:3px;top:2px;width:7px;height:7px;border-radius:50%;background:var(--orange)}
.badge-sep{width:1px;height:14px;background:var(--line)}

/* store */
.store{width:40px;height:12px;border-radius:2px;background:#111}

/* features */
.feature{position:absolute;width:72px}
.feature h4{margin:0 0 1px;font-size:5.4px;font-weight:700;color:var(--orange)}
.feature .body-text{font-size:4.3px;line-height:1.45}
.feature-icon{position:absolute;width:20px;height:20px;border-radius:50%;background:var(--orange);display:flex;align-items:center;justify-content:center}

/* phones */
.phone{position:absolute;width:40px;height:72px;border:2.5px solid var(--navy);border-radius:6px;background:#fff;box-sizing:border-box;overflow:hidden}
.phone .phone-bar{height:6px;background:var(--navy)}
.phone-body{padding:5px 4px;display:flex;flex-direction:column;gap:3px}
.phone-body i{display:block;height:2px;background:var(--soft)}
.phone-body i.field{height:5px;border:1px solid #cfd6de;background:#fff}
.phone-body i.btn{height:5px;background:var(--blue)}
.phone-body i.btn.alt{background:var(--orange)}
.phone-body i.qr{height:14px;width:14px;margin:0 auto;border:2px solid var(--navy);box-sizing:border-box}
.phone-body i.pic{height:18px;background:linear-gradient(135deg,#9aa3ae,#6c7785)}
.phone-body .keys{display:grid;grid-template-columns:repeat(4,1fr);gap:1.5px}
.phone-body .keys i{height:4px;background:#dfe4ea}
.phone-caption{position:absolute;width:60px;text-align:center;font-size:4.4px;line-height:1.4;color:var(--muted);margin:0}

/* thanks */
.contact{position:absolute;top:132px;width:80px;text-align:center;color:#fff;font-size:4.4px;line-height:1.4;font-weight:600}
.contact-icon{width:18px;height:18px;border-radius:50%;background:var(--orange);margin:0 auto 3px;display:flex;align-items:center;justify-content:center}
</style>
</head>
<body>

<svg class="defs" aria-hidden="true">
  <defs>
    <linearGradient id="navyGrad" x1="0" y1="0" x2="0" y2="1">
      <stop offset="0" stop-color="#04427a"/><stop offset="1" stop-color="#00345D"/>
    </linearGradient>
    <linearGradient id="cityGrad" x1="0" y1="0" x2="1" y2="1">
      <stop offset="0" stop-color="#0b3a6a"/><stop offset=".55" stop-color="#124a78"/><stop offset="1" stop-color="#002a4d"/>
    </linearGradient>
  </defs>
</svg>

<div class="stage"></div>

<!-- presentation cover shown large -->
<section class="slide hero">
  <svg class="fill" viewBox="0 0 347 195" preserveAspectRatio="none">
    <path fill="url(#navyGrad)" d="M0 0H347V100Q174 175 0 100Z"/>
    <path class="wave-orange" d="M0 104Q174 180 347 104"/>
    <path class="wave-grey" d="M0 111Q174 187 347 111"/>
  </svg>
  <h1 class="cover-title"><span class="accent">METER</span> MANAGEMENT</h1>
  <p class="cover-sub">LOWER YOUR COSTS BY AUTOMATING<br>ENERGY BILLING AND SETTLEMENT AND IMPROVE<br>TRANSPARANCY TO YOUR TENANTS.</p>
  <div class="logo" style="left:28px;top:152px"><span class="logo-dot"></span>Stroomwacht</div>
  <div class="partner" style="right:18px;top:152px"><span class="partner-dot"></span>GRIDLENS</div>
</section>

<!-- row 1 -->
<section class="slide c1 r1">
  <svg class="fill" viewBox="0 0 347 195" preserveAspectRatio="none">
    <path fill="url(#navyGrad)" d="M0 0H347V100Q174 175 0 100Z"/>
    <path class="wave-orange" d="M0 104Q174 180 347 104"/>
    <path class="wave-grey" d="M0 111Q174 187 347 111"/>
  </svg>
  <h1 class="cover-title"><span class="accent">METER</span> MANAGEMENT</h1>
  <p class="cover-sub">LOWER YOUR COSTS BY AUTOMATING<br>ENERGY BILLING AND SETTLEMENT AND IMPROVE<br>TRANSPARANCY TO YOUR TENANTS.</p>
  <div class="logo" style="left:28px;top:152px"><span class="logo-dot"></span>Stroomwacht</div>
  <div class="partner" style="right:14px;top:152px"><span class="partner-dot"></span>GRIDLENS</div>
</section>

<section class="slide c2 r1" style="border:1px solid #cfd3d8;box-sizing:border-box">
  <div class="logo" style="left:26px;top:26px"><span class="logo-dot"></span>Stroomwacht</div>
  <div class="partner" style="right:14px;top:16px"><span class="partner-dot"></span>GRIDLENS</div>
  <h2 class="abs" style="left:24px;top:84px;margin:0;font-size:12.5px;font-weight:800;color:var(--navy)">METER MANAGEMENT</h2>
  <p class="abs" style="left:24px;top:104px;margin:0;font-size:5.4px;line-height:1.55;font-weight:700;color:var(--navy)">LOWER YOUR COSTS BY AUTOMATING<br>ENERGY BILLING AND SETTLEMENT AND<br>IMPROVE TRANSPARANCY TO YOUR TENANTS.</p>
  <p class="abs" style="left:24px;top:170px;margin:0;font-size:5.8px;font-weight:700;color:var(--orange)">STROOMWACHT.NL</p>
  <svg class="abs" style="right:0;bottom:0" width="130" height="130" viewBox="0 0 130 130">
    <circle cx="130" cy="130" r="120" fill="var(--orange)"/>
  </svg>
</section>

<section class="slide c3 r1">
  <svg class="fill" viewBox="0 0 347 195" preserveAspectRatio="none" role="img" aria-label="City skyline photo in deep blue tones behind the title">
    <path fill="url(#cityGrad)" d="M0 0H347V100Q174 175 0 100Z"/>
    <path class="wave-orange" d="M0 104Q174 180 347 104"/>
    <path class="wave-grey" d="M0 111Q174 187 347 111"/>
  </svg>
  <h1 class="cover-title"><span class="accent">METER</span> MANAGEMENT</h1>
  <p class="cover-sub">LOWER YOUR COSTS BY AUTOMATING<br>ENERGY BILLING AND SETTLEMENT AND IMPROVE<br>TRANSPARANCY TO YOUR TENANTS.</p>
  <div class="logo" style="left:28px;top:152px"><span class="logo-dot"></span>Stroomwacht</div>
  <div class="partner" style="right:14px;top:152px"><span class="partner-dot"></span>GRIDLENS</div>
</section>

<!-- row 2 -->
<section class="slide c1 r2">
  <div class="fill" role="img" aria-label="Night photo of a city skyline with lit office towers" style="background:linear-gradient(180deg,#2c3d5c 0%,#1b2a47 55%,#0d1a30 100%)"></div>
  <svg class="fill" viewBox="0 0 347 195" preserveAspectRatio="none">
    <path fill="#fff" d="M0 0H347V18Q174 80 0 18Z"/>
    <path class="wave-orange" d="M0 21Q174 84 347 21"/>
  </svg>
  <div class="logo small" style="left:140px;top:22px;font-size:9px"><span class="logo-dot" style="width:10px;height:10px"></span>Stroomwacht</div>
  <h1 class="cover-title" style="top:127px;font-size:16px">METER MANAGEMENT</h1>
  <p class="cover-sub" style="top:149px;font-size:5.8px;font-weight:800">LOWER YOUR COSTS BY AUTOMATING<br>ENERGY BILLING AND SETTLEMENT AND IMPROVE<br>TRANSPARANCY TO YOUR TENANTS.</p>
</section>

<section class="slide c2 r2">
  <div class="logo small corner"><span class="logo-dot"></span>Stroomwacht</div>
  <h2 class="slide-heading" style="top:62px">INTRODUCTION</h2>
  <div class="abs" style="left:38px;top:86px;width:282px">
    <p class="body-text">Vastgoedeigenaren beheren vaak meerdere gebouwen met gedeelde voorzieningen zoals gas, water en elektriciteit. Deze kosten moeten eerlijk worden verdeeld over de huurders van kantoren en woningen. Huurders willen daarnaast graag inzicht in hun eigen verbruik, zodat zij bewuster met energie omgaan.</p>
  </div>
  <div class="slide-footer"><span class="footer-site">STROOMWACHT.NL</span><span class="footer-bar">Copyright © GridLens. All rights reserved</span><span class="footer-page">01</span></div>
</section>

<section class="slide c3 r2">
  <div class="logo small corner"><span class="logo-dot"></span>Stroomwacht</div>
  <h2 class="slide-heading rule"><span class="accent">HOE WERKT</span><br>STROOMWACHT?</h2>
  <div class="laptop" role="img" aria-label="Laptop showing the energy dashboard with usage charts" style="left:34px;top:80px;width:140px;height:82px">
    <div class="lid"><div class="ui">
      <div class="ui-side"><i class="on"></i><i></i><i></i><i></i><i></i></div>
      <div class="ui-main"><span class="ui-top"></span><div class="ui-cards"><i></i><i></i><i></i></div>
        <div class="ui-chart"><i style="height:40%"></i><i style="height:55%"></i><i style="height:35%"></i><i style="height:70%"></i><i style="height:50%"></i><i style="height:85%"></i><i style="height:60%"></i><i style="height:45%"></i><i style="height:75%"></i><i style="height:65%"></i></div></div>
    </div></div>
    <div class="base"></div>
  </div>
  <div class="abs" style="left:186px;top:80px;width:146px">
    <h3 class="sub-heading">Het dashboard</h3>
    <p class="body-text">Het dashboard van Stroomwacht is online te bereiken via elke browser. Elke meter en periode is eenvoudig te selecteren.</p>
    <p class="body-text">Nieuwe meters en gebouwen voegt u snel toe. Per meter stelt u prognoses en rapportages in.</p>
  </div>
  <div class="slide-footer"><span class="footer-site">STROOMWACHT.NL</span><span class="footer-bar">Copyright © GridLens. All rights reserved</span><span class="footer-page">01</span></div>
</section>

<!-- row 3 -->
<section class="slide c1 r3">
  <div class="logo small corner"><span class="logo-dot"></span>Stroomwacht</div>
  <h2 class="slide-heading"><span class="accent">HOE WERKT</span><br>STROOMWACHT?</h2>
  <div class="ui" role="img" aria-label="Screenshot of the meter list in the web portal" style="left:34px;top:68px;width:142px;height:70px">
    <div class="ui-side"><i></i><i class="on"></i><i></i><i></i><i></i><i></i></div>
    <div class="ui-main"><span class="ui-top"></span><span class="ui-row"></span><span class="ui-row short"></span><span class="ui-row"></span><span class="ui-row short"></span><span class="ui-row"></span><span class="ui-row short"></span><span class="ui-row"></span><span class="ui-row short"></span></div>
  </div>
  <div class="abs" style="left:187px;top:64px;width:146px">
    <h3 class="sub-heading">Meters toevoegen<br>en beheren</h3>
    <p class="body-text">U voegt zelf slimme en analoge meters toe en beheert ze op één plek. Slimme meters worden automatisch gekoppeld.</p>
    <p class="body-text">Voor elke analoge meter maakt het systeem een QR-label dat u op de meter plakt.</p>
  </div>
  <div class="slide-footer"><span class="footer-site">STROOMWACHT.NL</span><span class="footer-bar">Copyright © GridLens. All rights reserved</span><span class="footer-page">01</span></div>
</section>

<section class="slide c2 r3">
  <div class="logo small corner"><span class="logo-dot"></span>Stroomwacht</div>
  <h2 class="slide-heading"><span class="accent">HOE WERKT</span><br>STROOMWACHT?</h2>
  <div class="flow">
    <span class="flow-meter"><i></i><b></b></span>
    <span class="flow-step">01</span>
    <span class="flow-phone"><i></i></span>
    <span class="flow-step">02</span>
    <span class="flow-phone"><i class="dial"></i></span>
    <span class="flow-step">03</span>
    <span class="flow-screen"><i></i><i></i><i></i><i></i></span>
  </div>
  <div class="abs" style="left:38px;top:132px;width:282px">
    <h3 class="sub-heading">Analoge meterstand opnemen</h3>
    <p class="body-text">Een medewerker neemt de stand op locatie op. Met de mobiele app scant hij de QR-code en maakt een foto van de meter. Daarna gaat de stand direct naar het dashboard.</p>
  </div>
  <div class="slide-footer"><span class="footer-site">STROOMWACHT.NL</span><span class="footer-bar">Copyright © GridLens. All rights reserved</span><span class="footer-page">01</span></div>
</section>

<section class="slide c3 r3">
  <div class="logo small corner"><span class="logo-dot"></span>Stroomwacht</div>
  <h2 class="slide-heading"><span class="accent">HOE WERKT</span><br>STROOMWACHT?</h2>
  <div class="ui" role="img" aria-label="Screenshot of a submitted meter reading with photo" style="left:30px;top:74px;width:140px;height:62px">
    <div class="ui-side"><i></i><i></i><i class="on"></i><i></i><i></i></div>
    <div class="ui-main"><span class="ui-top"></span><span class="ui-photo"></span><span class="ui-row"></span><span class="ui-row short"></span><span class="ui-row"></span></div>
  </div>
  <div class="abs" style="left:186px;top:70px;width:146px">
    <h3 class="sub-heading">Analoge meterstand<br>verwerken</h3>
    <p class="body-text">Ingezonden standen zijn direct zichtbaar op het dashboard. Wijkt een stand af van de verwachting, dan volgt een controle.</p>
    <p class="body-text">De beheerder corrigeert de stand eenvoudig aan de hand van de foto.</p>
  </div>
  <div class="slide-footer"><span class="footer-site">STROOMWACHT.NL</span><span class="footer-bar">Copyright © GridLens. All rights reserved</span><span class="footer-page">01</span></div>
</section>

<!-- row 4 -->
<section class="slide c1 r4">
  <div class="logo small corner"><span class="logo-dot"></span>Stroomwacht</div>
  <h2 class="slide-heading">WE SUPPORT</h2>
  <div class="abs" style="left:38px;top:54px;width:280px">
    <h3 class="sub-heading" style="font-size:7px">Stroomwacht ondersteunt alle slimme meters</h3>
    <p class="body-text">Stroomwacht is gecertificeerd voor landelijke meetdata en leest alle slimme meters voor kleinverbruik uit.</p>
    <p class="body-text">Grootverbruik lezen we uit samen met een erkend meetbedrijf voor elektra en gas.</p>
    <p class="body-text">Via API-koppelingen zetten we meetdata om in heldere rapportages.</p>
  </div>
  <div class="badges">
    <span class="badge"></span><span class="badge-sep"></span>
    <span class="badge"></span><span class="badge-sep"></span>
    <span class="badge"></span><span class="badge-sep"></span>
    <span class="badge"></span>
  </div>
  <div class="slide-footer"><span class="footer-site">STROOMWACHT.NL</span><span class="footer-bar">Copyright © GridLens. All rights reserved</span><span class="footer-page">01</span></div>
</section>

<section class="slide c2 r4">
  <div class="logo small corner"><span class="logo-dot"></span>Stroomwacht</div>
  <h2 class="slide-heading">DE VOORDELEN</h2>
  <div class="benefits">
    <div class="benefit">
      <div class="benefit-icon">
        <svg width="34" height="30" viewBox="0 0 34 30"><circle cx="9" cy="22" r="6" fill="none" stroke="var(--navy)" stroke-width="1.5"/><circle cx="25" cy="22" r="6" fill="none" stroke="var(--navy)" stroke-width="1.5"/><path d="M4 10L9 5L14 10V14H4Z" fill="var(--navy)"/><path d="M20 14V8L24 10V8L28 10V14Z" fill="var(--navy)"/></svg>
      </div>
      <h3>Gemak</h3>
      <p class="tag">met alle soort energiemeters<br>op één dashboard</p>
      <p class="body-text">Klein- en grootverbruik meters op één plek. Analoge meters neemt u op met de app.</p>
    </div>
    <div class="benefit">
      <div class="benefit-icon"><span class="bar" style="height:10px"></span><span class="bar" style="height:14px"></span><span class="bar" style="height:12px"></span><span class="bar" style="height:18px"></span><span class="bar" style="height:22px;background:var(--orange)"></span><span class="bar" style="height:26px"></span></div>
      <h3>Risicomanagement</h3>
      <p class="tag">met signalering van<br>overstijging van prognoses</p>
      <p class="body-text">Een melding zodra het jaarverbruik boven de prognose dreigt te komen.</p>
    </div>
    <div class="benefit">
      <div class="benefit-icon">
        <svg width="24" height="30" viewBox="0 0 24 30"><rect x="2" y="1" width="20" height="28" rx="2" fill="none" stroke="var(--navy)" stroke-width="1.8"/><rect x="6" y="16" width="2.5" height="8" fill="var(--navy)"/><rect x="11" y="12" width="2.5" height="12" fill="var(--navy)"/><rect x="16" y="9" width="2.5" height="15" fill="var(--navy)"/></svg>
      </div>
      <h3>Tijdsbesparing</h3>
      <p class="tag">met automatisch<br>rapportages voor huurders</p>
      <p class="body-text">Huurders ontvangen automatisch hun eigen verbruiksrapportage.</p>
    </div>
  </div>
  <div class="slide-footer"><span class="footer-site">STROOMWACHT.NL</span><span class="footer-bar">Copyright © GridLens. All rights reserved</span><span class="footer-page">01</span></div>
</section>

<section class="slide c3 r4">
  <div class="logo small corner"><span class="logo-dot"></span>Stroomwacht</div>
  <h2 class="slide-heading">DE VOORDELEN</h2>
  <div class="benefits">
    <div class="benefit">
      <div class="benefit-icon">
        <svg width="34" height="30" viewBox="0 0 34 30"><path d="M2 2V28H32" fill="none" stroke="var(--navy)" stroke-width="1.2"/><path d="M4 24Q12 22 16 18T30 12" fill="none" stroke="var(--navy)" stroke-width="1.5"/><circle cx="28" cy="6" r="2" fill="var(--orange)"/></svg>
      </div>
      <h3>Kostenbesparing</h3>
      <p class="tag">met piekverbruiksignalering<br>per aansluiting</p>
      <p class="body-text">Een melding zodra het dagverbruik boven een limiet komt.</p>
    </div>
    <div class="benefit">
      <div class="benefit-icon">
        <svg width="34" height="30" viewBox="0 0 34 30"><circle cx="17" cy="15" r="13" fill="none" stroke="var(--navy)" stroke-width="1.5"/><path d="M6 28V18M10 28V14M14 28V16M18 28V12M22 28V15M26 28V18" stroke="var(--navy)" stroke-width="2"/></svg>
      </div>
      <h3>Inzicht</h3>
      <p class="tag">met verbruiksgegevens per<br>kwartier indien nodig</p>
      <p class="body-text">Slimme meters uitgelezen op kwartierniveau voor diepte-analyse.</p>
    </div>
    <div class="benefit">
      <div class="benefit-icon">
        <svg width="30" height="30" viewBox="0 0 30 30"><rect x="4" y="4" width="22" height="22" rx="3" fill="none" stroke="var(--navy)" stroke-width="1.8"/><path d="M9 15l4 4 8-9" fill="none" stroke="var(--orange)" stroke-width="2.2"/></svg>
      </div>
      <h3>Maatwerk</h3>
      <p class="tag">omdat uw klanten unieke wensen<br>hebben waar u aan wilt voldoen</p>
      <p class="body-text">Wij denken graag mee over een oplossing op maat.</p>
    </div>
  </div>
  <div class="slide-footer"><span class="footer-site">STROOMWACHT.NL</span><span class="footer-bar">Copyright © GridLens. All rights reserved</span><span class="footer-page">01</span></div>
</section>

<!-- row 5 -->
<section class="slide c1 r5">
  <div class="abs" role="img" aria-label="Desk photo with calculator, coins and financial charts" style="left:0;top:0;width:347px;height:120px;background:linear-gradient(135deg,#c9ced6,#a9b1bc 55%,#8e98a6)"></div>
  <div class="abs" style="left:0;top:110px;width:347px;height:85px;background:#fff"></div>
  <div class="laptop" style="left:28px;top:64px;width:184px;height:112px">
    <div class="lid" style="padding:5px"><div style="width:100%;height:100%;background:#fff"></div></div>
    <div class="base"></div>
  </div>
  <div class="logo" style="left:64px;top:106px;font-size:14px"><span class="logo-dot"></span>Stroomwacht</div>
  <div class="phone" style="left:196px;top:104px;width:34px;height:64px;border-color:#1d1f22;border-radius:5px"><div class="phone-bar" style="background:#1d1f22"></div><div class="phone-body"><i class="btn alt"></i><i></i><i></i><i class="btn"></i></div></div>
  <p class="body-text abs" style="left:238px;top:146px;width:100px;text-align:center;font-size:4.6px">Geen pakket past 100% bij u en uw klanten. Daarom denken wij graag mee over maatwerk.</p>
</section>

<section class="slide c2 r5" style="background:#f3f4f6">
  <svg class="fill" viewBox="0 0 347 195" preserveAspectRatio="none">
    <path fill="url(#navyGrad)" d="M0 0H347V120Q230 168 0 138Z"/>
    <path class="wave-orange" d="M0 142Q230 172 347 124"/>
  </svg>
  <div class="abs" role="img" aria-label="Hand holding a smartphone with the Stroomwacht app" style="left:0;top:40px;width:120px;height:155px;background:linear-gradient(160deg,#d9b8a0,#b98f74);clip-path:polygon(30% 0,100% 0,100% 100%,0 100%,0 30%)"></div>
  <h2 class="abs" style="left:160px;top:26px;margin:0;font-size:12px;font-weight:800;line-height:1.1;color:#fff">DOWNLOAD DE<br>MOBIELE APP</h2>
  <p class="abs" style="left:160px;top:60px;margin:0;width:172px;font-size:5.4px;font-weight:700;line-height:1.45;color:#fff">Download de mobiele app van Stroomwacht voor het opnemen van analoge meterstanden. Klik op de button om de gewenste app store te openen.</p>
  <div class="abs" style="left:250px;top:167px;display:flex;gap:4px"><span class="store"></span><span class="store"></span></div>
</section>

<section class="slide c3 r5">
  <div class="logo small corner"><span class="logo-dot"></span>Stroomwacht</div>
  <h2 class="slide-heading">BESTE EIGENSCHAPPEN</h2>
  <svg class="abs" style="left:104px;top:42px" width="140" height="120" viewBox="0 0 140 120"><circle cx="70" cy="64" r="52" fill="none" stroke="#e2e5e9" stroke-width="1"/></svg>
  <div class="phone" style="left:154px;top:60px;width:40px;height:78px;border-radius:7px"><div class="phone-bar"></div><div class="phone-body"><i class="btn alt"></i><i></i><i class="short"></i><i></i><i class="btn"></i></div></div>
  <span class="feature-icon" style="left:117px;top:62px"><svg width="10" height="10" viewBox="0 0 24 24"><path fill="#fff" d="M12 2a7 7 0 00-4 12.7V18h8v-3.3A7 7 0 0012 2zM9 20h6v2H9z"/></svg></span>
  <span class="feature-icon" style="left:211px;top:62px"><svg width="10" height="10" viewBox="0 0 24 24"><path fill="#fff" d="M3 6h18v14H3zM16 12h4v4h-4z"/></svg></span>
  <span class="feature-icon" style="left:113px;top:120px"><svg width="10" height="10" viewBox="0 0 24 24"><circle cx="12" cy="12" r="9" fill="none" stroke="#fff" stroke-width="2.5"/><path d="M12 7v5l3 3" fill="none" stroke="#fff" stroke-width="2.5"/></svg></span>
  <span class="feature-icon" style="left:213px;top:120px"><svg width="10" height="10" viewBox="0 0 24 24"><path fill="#fff" d="M6 10V8a6 6 0 0112 0v2h1v12H5V10zm3 0h6V8a3 3 0 00-6 0z"/></svg></span>
  <div class="feature" style="left:32px;top:56px;text-align:center"><h4>Eigenschappen</h4><p class="body-text">Een melding zodra het dagverbruik boven een limiet komt.</p></div>
  <div class="feature" style="left:245px;top:56px;text-align:center"><h4>Eigenschappen</h4><p class="body-text">Een melding zodra het dagverbruik boven een limiet komt.</p></div>
  <div class="feature" style="left:30px;top:118px;text-align:center"><h4>Eigenschappen</h4><p class="body-text">Een melding zodra het dagverbruik boven een limiet komt.</p></div>
  <div class="feature" style="left:245px;top:118px;text-align:center"><h4>Eigenschappen</h4><p class="body-text">Een melding zodra het dagverbruik boven een limiet komt.</p></div>
  <div class="slide-footer"><span class="footer-site">STROOMWACHT.NL</span><span class="footer-bar">Copyright © GridLens. All rights reserved</span><span class="footer-page">01</span></div>
</section>

<!-- row 6 -->
<section class="slide c1 r6">
  <h2 class="slide-heading" style="left:26px;top:16px">HOE TE GEBRUIKEN</h2>
  <div class="abs" style="left:0;top:64px;width:347px;height:60px;background:var(--orange)"></div>
  <div class="abs" style="left:0;top:124px;width:347px;height:6px;background:var(--navy)"></div>
  <div class="phone" style="left:26px;top:46px;height:80px"><div class="phone-bar"></div><div class="phone-body"><i class="btn alt"></i><i class="field"></i><i class="field"></i><i class="btn"></i><i></i></div></div>
  <div class="phone" style="left:104px;top:46px;height:80px"><div class="phone-bar"></div><div class="phone-body"><i></i><i class="qr"></i><i class="btn"></i><i class="btn alt"></i></div></div>
  <div class="phone" style="left:182px;top:46px;height:80px"><div class="phone-bar"></div><div class="phone-body"><i class="field"></i><i class="btn"></i><div class="keys"><i></i><i></i><i></i><i></i><i></i><i></i><i></i><i></i><i></i><i></i><i></i><i></i></div></div></div>
  <div class="phone" style="left:260px;top:46px;height:80px"><div class="phone-bar"></div><div class="phone-body"><i></i><i class="pic"></i><i class="btn"></i></div></div>
  <p class="phone-caption" style="left:16px;top:140px">Log in met uw account</p>
  <p class="phone-caption" style="left:94px;top:140px">Scan de QR-code op de meter</p>
  <p class="phone-caption" style="left:172px;top:140px">Voer de meterstand in</p>
  <p class="phone-caption" style="left:250px;top:140px">Maak een foto en verstuur</p>
</section>

<section class="slide c2 r6">
  <h2 class="slide-heading" style="left:26px;top:16px">HOE TE GEBRUIKEN</h2>
  <div class="abs" style="left:0;top:64px;width:347px;height:60px;background:var(--orange)"></div>
  <div class="abs" style="left:0;top:124px;width:200px;height:6px;background:var(--navy)"></div>
  <div class="phone" style="left:26px;top:44px;height:86px"><div class="phone-bar"></div><div class="phone-body"><i class="pic"></i><div class="keys"><i></i><i></i><i></i><i></i><i></i><i></i><i></i><i></i></div><i class="btn"></i></div></div>
  <div class="phone" style="left:104px;top:44px;height:86px"><div class="phone-bar"></div><div class="phone-body"><i class="field"></i><i class="field"></i><i></i><i class="pic"></i><i class="btn"></i></div></div>
  <p class="phone-caption" style="left:16px;top:142px">Stand en foto controleren</p>
  <p class="phone-caption" style="left:94px;top:142px">Opname versturen</p>
  <div class="ui" role="img" aria-label="Screenshot of a meter reading with photo" style="left:210px;top:10px;width:118px;height:52px">
    <div class="ui-main"><span class="ui-top"></span><span class="ui-photo"></span><span class="ui-row"></span><span class="ui-row short"></span></div>
  </div>
  <p class="abs" style="left:210px;top:74px;width:118px;margin:0;text-align:center;font-size:4.4px;color:#fff;line-height:1.4">De stand verschijnt direct in het portaal</p>
  <div class="ui" role="img" aria-label="Screenshot of the dashboard usage charts" style="left:210px;top:100px;width:118px;height:62px">
    <div class="ui-side"><i class="on"></i><i></i><i></i><i></i></div>
    <div class="ui-main"><span class="ui-top"></span><div class="ui-cards"><i></i><i></i></div><div class="ui-chart"><i style="height:40%"></i><i style="height:65%"></i><i style="height:50%"></i><i style="height:80%"></i><i style="height:55%"></i><i style="height:70%"></i></div></div>
  </div>
  <p class="phone-caption" style="left:210px;top:170px;width:118px">Verbruik direct zichtbaar op het dashboard</p>
</section>

<section class="slide c3 r6" style="background:var(--navy)">
  <svg class="fill" viewBox="0 0 347 195" preserveAspectRatio="none">
    <path fill="#fff" d="M0 0H347V22Q174 78 0 22Z"/>
    <path class="wave-orange" d="M0 26Q174 82 347 26"/>
  </svg>
  <div class="logo" style="left:126px;top:20px;font-size:11px"><span class="logo-dot" style="width:12px;height:12px"></span>Stroomwacht</div>
  <h2 class="abs" style="left:0;top:80px;width:100%;margin:0;text-align:center;font-size:13px;font-weight:800;color:#fff">THANK YOU</h2>
  <p class="abs" style="left:50px;top:100px;width:247px;margin:0;text-align:center;font-size:4.6px;line-height:1.5;color:#dfe7ef">Wij helpen vastgoedeigenaren en beheerders met heldere energiedata en eerlijke afrekening voor huurders.</p>
  <div class="contact" style="left:34px">
    <div class="contact-icon"><svg width="10" height="10" viewBox="0 0 24 24"><path fill="#fff" d="M6.6 10.8a15 15 0 006.6 6.6l2.2-2.2c.3-.3.7-.4 1-.2 1.1.4 2.3.6 3.6.6.6 0 1 .4 1 1V20c0 .6-.4 1-1 1A17 17 0 013 4c0-.6.4-1 1-1h3.5c.6 0 1 .4 1 1 0 1.3.2 2.5.6 3.6.1.3 0 .7-.2 1z"/></svg></div>
    31 6 120 45 880
  </div>
  <div class="contact" style="left:133px">
    <div class="contact-icon"><svg width="10" height="10" viewBox="0 0 24 24"><path fill="#fff" d="M12 2a7 7 0 00-7 7c0 5 7 13 7 13s7-8 7-13a7 7 0 00-7-7zm0 9.5A2.5 2.5 0 1112 6.5a2.5 2.5 0 010 5z"/></svg></div>
    Kanaalweg 12<br>1000 AB Amsterdam
  </div>
  <div class="contact" style="left:232px">
    <div class="contact-icon"><svg width="10" height="10" viewBox="0 0 24 24"><path fill="#fff" d="M3 5h18v14H3zm2 2v.5l7 4.5 7-4.5V7l-7 4.5z"/></svg></div>
    info@stroomwacht.nl
  </div>
</section>

</body>
</html>
```